Selbsthilfegruppe für organtransplantierte Personen sucht Flyer-Design
Sehr schnelle Reaktion auf Änderungswünsche und top Support bis zum Druck :) Gerne wieder!
Zielgruppe
Wir sind eine Selbsthilfegruppe für organtransplantierte Personen, Zielgruppe sind Personen aus der Region die auch ein Spenderorgan empfangen haben und deren Angehörige, die Beistand und Information suchen sowie gemeinsame Aktivitäten wahrnehmen möchten.
Aufgabenstellung
Es gibt bereits einen Flyer der jedoch überarbeitet und etwas schöner und moderner gestaltet werden soll. Der Text kann bestehen bleiben und die Aufteilung muss nicht zwingend geändert werden, anstelle der aktuellen Fotos sollen dann andere eingefügt werden, die übergeben werden, sobald das Design akzeptiert wurde. Es geht hauptsächlich um das Design selbst, es soll ansprechen, freundlich, modern und hoffnungsvoll sein, die Grundfarbe sollte grün sein. Das Logo kann beibehalten aber farblich auch gerne angepasst werden. Es soll ein normaler Faltflyer sein, 2 Faltungen und damit vorn und hinten je 3 einzelne Bereiche wie aktuell, Gesamtmaß A4. Bei Rückfragen gerne melden!

```html
<!DOCTYPE html>
<html lang="de">
<head>
<meta charset="utf-8">
<title>Flyer Selbsthilfegruppe – Innenseite</title>
<link href="https://fonts.googleapis.com/css2?family=Quicksand:wght@500;700&family=Pinyon+Script&display=swap" rel="stylesheet">
<style>
  :root {
    --backdrop: #a3a3a3;
    --paper: #ffffff;
    --green: #3f8f2f;
    --green-mid: #5f9e36;
    --orange: #df9420;
    --gold: #d9a52b;
    --script: #d68a1c;
    --photo-skin: #c9a184;
    --photo-light: #e7ddd3;
  }
  * { margin: 0; padding: 0; box-sizing: border-box; }
  html, body { width: 1200px; height: 675px; overflow: hidden; }
  body { background: var(--backdrop); font-family: "Quicksand", sans-serif; }

  .flyer {
    position: absolute; left: 134px; top: 8px;
    width: 932px; height: 659px;
    background: var(--paper); overflow: hidden;
  }
  .flyer__bands { position: absolute; inset: 0; }

  .hands-photo {
    position: absolute; left: 622px; top: 0; width: 310px; height: 540px;
    background: linear-gradient(160deg, var(--photo-light) 0%, var(--photo-skin) 45%, #b98a6c 70%, #d8d4d0 100%);
  }

  .script-title {
    position: absolute; font-family: "Pinyon Script", cursive;
    color: var(--script); font-size: 40px; line-height: 1;
    border-bottom: 1px solid var(--script); padding: 0 2px 1px;
  }
  .script-title--about { left: 154px; top: 70px; }
  .script-title--together { left: 388px; top: 22px; }

  .about { position: absolute; left: 31px; top: 124px; width: 300px; }
  .about__block { margin-bottom: 20px; }
  .about__head { color: var(--green); font-weight: 700; font-size: 16px; line-height: 20px; }
  .about__text { color: var(--orange); font-weight: 500; font-size: 16px; line-height: 20px; }

  .activity-photo {
    position: absolute; left: 353px; width: 210px; height: 134px;
    border: 3px solid var(--green-mid); border-radius: 8px;
  }
  .activity-photo--inform { top: 74px; background: linear-gradient(135deg, #6aa24a, #d9c9a8 55%, #c7d84a); }
  .activity-photo--discuss { top: 232px; background: linear-gradient(135deg, #a5735a, #efece8 45%, #8a8580); }
  .activity-photo--celebrate { top: 390px; background: linear-gradient(135deg, #c9b79c, #f2ede6 50%, #7a8a5a); }

  .caption { position: absolute; color: var(--orange); font-weight: 500; font-size: 16px; line-height: 20px; }
  .caption--inform { left: 353px; width: 210px; text-align: right; top: 206px; }
  .caption--discuss { left: 353px; top: 366px; }
  .caption--celebrate { left: 353px; top: 524px; }

  .outreach {
    position: absolute; left: 640px; width: 272px; top: 554px;
    color: #fff; font-weight: 500; font-size: 15.5px; line-height: 20px; text-align: center;
  }
</style>
</head>
<body>
  <div class="flyer">
    <div class="hands-photo" role="img" aria-label="Foto: viele Hände übereinander gelegt als Zeichen der Gemeinschaft"></div>

    <svg class="flyer__bands" width="932" height="659" viewBox="0 0 932 659">
      <defs>
        <linearGradient id="topBand" x1="0" y1="0" x2="1" y2="0">
          <stop offset="0" stop-color="#e59a28"/>
          <stop offset="0.45" stop-color="#84a63a"/>
          <stop offset="1" stop-color="#4d9a35"/>
        </linearGradient>
        <linearGradient id="bottomBand" x1="0" y1="0" x2="1" y2="0">
          <stop offset="0" stop-color="#43963a"/>
          <stop offset="0.55" stop-color="#6ea13a"/>
          <stop offset="1" stop-color="#dca52b"/>
        </linearGradient>
      </defs>
      <path d="M0,0 H436 C260,30 70,80 0,122 Z" fill="url(#topBand)"/>
      <path d="M0,600 C320,560 720,520 932,418 V659 H0 Z" fill="url(#bottomBand)"/>
    </svg>

    <h2 class="script-title script-title--about">Über uns</h2>
    <section class="about">
      <div class="about__block">
        <p class="about__head">Wir sind ...</p>
        <p class="about__text">eine Gruppe von Betroffenen<br>und deren Angehörige.</p>
      </div>
      <div class="about__block">
        <p class="about__head">Wir möchten ...</p>
        <p class="about__text">Erfahrungen austauschen,<br>Fachvorträge besuchen, aber nicht<br>nur über Krankheit reden, sondern<br>auch miteinander fröhlich sein.</p>
      </div>
      <div class="about__block">
        <p class="about__head">Wir organisieren gemeinsam ...</p>
        <p class="about__text">regelmäßige Treffen, Fachvorträge,<br>Infoveranstaltungen, gesellige<br>Zusammenkünfte und einiges mehr.</p>
      </div>
      <div class="about__block">
        <p class="about__head">Wir treffen uns ...</p>
        <p class="about__text">regelmäßig am letzten Dienstag<br>des Monats um 15:00 Uhr im<br>Familienzentrum ‚Lindenhof‘,<br>Wiesengrund 12 in<br>Talbrunn.</p>
      </div>
    </section>

    <h2 class="script-title script-title--together">Gemeinsam</h2>
    <div class="activity-photo activity-photo--inform" role="img" aria-label="Foto: Gruppe an einem Infostand mit Broschüren"></div>
    <p class="caption caption--inform">... informieren</p>
    <div class="activity-photo activity-photo--discuss" role="img" aria-label="Foto: Gesprächsrunde im Stuhlkreis"></div>
    <p class="caption caption--discuss">... diskutieren</p>
    <div class="activity-photo activity-photo--celebrate" role="img" aria-label="Foto: Gruppenbild bei einem geselligen Ausflug"></div>
    <p class="caption caption--celebrate">... feiern</p>

    <p class="outreach">... wollen wir mit öffentlichen<br>Aktionen viele Menschen erreichen<br>und über unsere Arbeit informieren.</p>
  </div>
</body>
</html>
```